Business Card Design

Maple Crest Rentals
Maple Crest Rentals is a high end home rental leasing company that provides exquisite properties in niche markets. We are a small family owned business that considers our clients not as renters, but as friends. Every property we buy must be brought up to our high standards before it is offered on the market. The properties that we lease are exceptional, "move in" ready homes. This allows for the client to take pride in their lease as if it was their own home. To put it another way; we do not lease a property that we would not live in ourselves.

Target Market(s)

Couples making $100K or more

Industry/Entity Type

Business

Requirements
Must have
• Some sort of logo
Nice to have
• good slogan
Should not have
• Pink

```html
<!DOCTYPE html>
<html lang="en">
<head>
<meta charset="utf-8">
<title>Maple Crest Rentals — Business Card</title>
<link rel="stylesheet" href="https://fonts.googleapis.com/css2?family=Fira+Sans:wght@300;600;700&display=swap">
<style>
  :root {
    --paper: #ffffff;
    --ink-strong: #454545;
    --ink-dark: #2f2f2f;
    --ink-body: #3a3a3a;
    --accent: #1f8fc0;
  }
  * { margin: 0; padding: 0; box-sizing: border-box; }
  html, body {
    width: 1200px; height: 687px; overflow: hidden;
    background: var(--paper);
  }
  .card {
    position: relative;
    width: 1200px; height: 687px;
    background: var(--paper);
    font-family: "Fira Sans", sans-serif;
    color: var(--ink-body);
  }
  .brand-mark {
    position: absolute;
    left: 560px; top: 40px;
    width: 80px; height: 80px;
    background: var(--accent);
  }
  .brand-name {
    position: absolute;
    left: 0; right: 0; top: 208px;
    text-align: center;
    font-weight: 700;
    font-size: 80px;
    line-height: 1;
    letter-spacing: 1px;
    color: var(--ink-strong);
  }
  .rule {
    position: absolute;
    height: 4px;
    background: var(--ink-strong);
  }
  .rule--long { left: 420px; width: 378px; top: 318px; }
  .rule--short { left: 548px; width: 101px; top: 374px; }
  .tagline {
    position: absolute;
    left: 0; right: 0; top: 332px;
    text-align: center;
    font-weight: 600;
    font-size: 29px;
    letter-spacing: 0.5px;
    color: var(--ink-dark);
  }
  .services {
    position: absolute;
    left: 0; right: 0; top: 414px;
    text-align: center;
    font-weight: 300;
    font-size: 31px;
    line-height: 46px;
    color: var(--ink-body);
  }
  .contact {
    position: absolute;
    top: 582px;
    font-weight: 300;
    font-size: 31px;
    line-height: 45px;
    color: var(--ink-body);
  }
  .contact--person { left: 42px; }
  .contact--details { left: 760px; }
</style>
</head>
<body>
  <main class="card">
    <div class="brand-mark" aria-hidden="true"></div>
    <h1 class="brand-name">MAPLE CREST RENTALS</h1>
    <div class="rule rule--long"></div>
    <p class="tagline">Easy Rental. Excellent Living</p>
    <div class="rule rule--short"></div>
    <p class="services">
      Property Services, Professional Home Rental Leasing Services,<br>
      Construction Services, Property Management Services,<br>
      Relocation Services
    </p>
    <div class="contact contact--person">
      <p class="contact-name">Daniel Hartwell</p>
      <p class="contact-role">Director</p>
    </div>
    <div class="contact contact--details">
      <p class="contact-phone">Tel : +123 555 0182</p>
      <p class="contact-address">#27, Elm Avenue, Portland</p>
    </div>
  </main>
</body>
</html>
```